Letter head for peronal trainer

Letter head top and bottom. Elite looking design that looks modern and prestigious for high end clients. Black, silver, reds etc. Attached are my business cards (2 x pdfs) and my website is: www.dariomokhtar.net for style/ideas

Needs to look good when printing and be locked onto the page when people use my word docs on the computer, I don't want it to be 'clickable' if you know what I mean. Needs to work in A4 in portrait (and in landscape, for programme cards). I need it to be editable for when I adjust the text myself. Needs my contact details and social media details and title personal trainer (Central London/Greenwich/Blackheath) and Online Distance Coaching. . A little picture at the bottom too if it works (Like the vest one)

```html
<!DOCTYPE html>
<html lang="en">
<head>
<meta charset="utf-8">
<title>Dario Mokhtar – Personal Trainer Letterhead</title>
<link rel="stylesheet" href="https://fonts.googleapis.com/css2?family=Archivo:ital,wght@0,400;0,700;0,900;1,400;1,900&display=swap">
<style>
  :root {
    --backdrop: #e6e6e6;
    --paper: #ffffff;
    --ink: #111111;
    --ink-soft: #222222;
    --brand-red: #c8202a;
    --rule-grey: #d4d4d4;
    --photo-light: #eef0f2;
    --photo-mid: #d3d6db;
    --portrait-tone: #dcdcdc;
  }
  * { box-sizing: border-box; margin: 0; padding: 0; }
  html, body {
    width: 1091px;
    height: 1200px;
    overflow: hidden;
    background: var(--backdrop);
    font-family: "Archivo", Arial, sans-serif;
  }
  .letterhead {
    position: absolute;
    left: 142px;
    top: 29px;
    width: 806px;
    height: 1142px;
    background: var(--paper);
    box-shadow: 0 4px 14px rgba(0,0,0,0.18);
    overflow: hidden;
  }
  .portrait {
    position: absolute;
    left: 23px;
    top: 17px;
    width: 160px;
    height: 244px;
    background: linear-gradient(180deg, var(--portrait-tone) 0%, var(--portrait-tone) 55%, rgba(255,255,255,0) 100%);
    opacity: 0.8;
  }
  .masthead {
    position: absolute;
    right: 30px;
    top: 50px;
    text-align: right;
  }
  .masthead__name {
    font-weight: 900;
    font-style: italic;
    font-size: 57px;
    line-height: 1;
    letter-spacing: 2px;
    color: var(--ink);
  }
  .masthead__title {
    margin-top: 14px;
    font-weight: 400;
    font-style: italic;
    font-size: 41px;
    line-height: 1;
    letter-spacing: 3px;
    color: var(--ink);
  }
  .masthead__areas {
    margin-top: 18px;
    font-weight: 400;
    font-size: 20px;
    line-height: 1;
    letter-spacing: 2px;
    color: var(--ink-soft);
  }
  .feature-photo {
    position: absolute;
    left: 450px;
    top: 667px;
    width: 356px;
    height: 475px;
    background:
      linear-gradient(180deg, rgba(255,255,255,1) 0%, rgba(255,255,255,0) 30%),
      linear-gradient(90deg, rgba(255,255,255,1) 0%, var(--photo-light) 35%, var(--photo-mid) 100%);
  }
  .badge {
    position: absolute;
    right: 8px;
    bottom: 10px;
    width: 108px;
    height: 108px;
    border-radius: 50%;
    border: 3px solid rgba(255,255,255,0.9);
  }
  .tagline {
    position: absolute;
    left: 15px;
    top: 1012px;
    font-weight: 400;
    font-size: 24px;
    line-height: 1;
    letter-spacing: 2px;
    color: var(--ink);
  }
  .tagline-rule {
    position: absolute;
    left: 0;
    top: 1047px;
    width: 560px;
    height: 5px;
    background: linear-gradient(90deg, var(--brand-red) 0%, var(--brand-red) 60%, rgba(200,32,42,0) 100%);
  }
  .tagline-rule::after {
    content: "";
    position: absolute;
    left: 0;
    top: 7px;
    width: 480px;
    height: 2px;
    background: linear-gradient(90deg, var(--rule-grey) 0%, rgba(212,212,212,0) 100%);
  }
  .contact-list {
    position: absolute;
    left: 20px;
    top: 1072px;
    width: 470px;
    display: grid;
    grid-template-columns: 286px 1fr;
    row-gap: 10px;
    list-style: none;
  }
  .contact-list__item {
    display: flex;
    align-items: center;
    gap: 16px;
    font-size: 15px;
    line-height: 18px;
    letter-spacing: 0.5px;
    color: var(--brand-red);
    white-space: nowrap;
  }
  .contact-list__icon {
    width: 14px;
    height: 14px;
    flex: none;
    fill: var(--brand-red);
  }
</style>
</head>
<body>
  <main class="letterhead">
    <div class="portrait" role="img" aria-label="Faded black and white portrait photo of the trainer"></div>

    <header class="masthead">
      <h1 class="masthead__name">DARIO MOKHTAR</h1>
      <p class="masthead__title">PERSONAL TRAINER</p>
      <p class="masthead__areas">CENTRAL LONDON/GREENWICH/BLACKHEATH</p>
    </header>

    <div class="feature-photo" role="img" aria-label="Faded photo of the trainer in a dark vest lifting a dumbbell">
      <div class="badge"></div>
    </div>

    <p class="tagline">ONLINE DISTANCE COACHING</p>
    <div class="tagline-rule"></div>

    <ul class="contact-list">
      <li class="contact-list__item">
        <svg class="contact-list__icon" viewBox="0 0 14 14" aria-hidden="true"><path d="M3 1 L5.5 1 L6.5 4 L5 5.3 C5.8 7 7 8.2 8.7 9 L10 7.5 L13 8.5 L13 11 C13 12 12 13 11 13 C5.5 12.6 1.4 8.5 1 3 C1 2 2 1 3 1 Z"/></svg>
        <span>0771842306</span>
      </li>
      <li class="contact-list__item">
        <svg class="contact-list__icon" viewBox="0 0 14 14" aria-hidden="true"><path d="M1 3 H13 V11 H1 Z M1.6 3.4 L7 7.6 L12.4 3.4" fill="var(--brand-red)" stroke="#fff" stroke-width="1"/></svg>
        <span>www.dariomokhtar.net</span>
      </li>
      <li class="contact-list__item">
        <svg class="contact-list__icon" viewBox="0 0 14 14" aria-hidden="true"><circle cx="7" cy="7" r="6"/><path d="M1.5 5.5 H12.5 M1.5 8.5 H12.5" stroke="#fff" stroke-width="1"/></svg>
        <span>mokhtar.darioPT@mailbox.com</span>
      </li>
      <li class="contact-list__item">
        <svg class="contact-list__icon" viewBox="0 0 14 14" aria-hidden="true"><circle cx="7" cy="7" r="6"/></svg>
        <span>@mokhy_2</span>
      </li>
    </ul>
  </main>
</body>
</html>
```